Professional PowerPoint Template for Data Reports, Presentations

We are a small leadership coaching/consulting firm and would like to update our PowerPoint template that we use with our clients, who are typically mid-senior level company professionals. I've attached a sample Powerpoint as well as our branding guide. The cover page is what needs the most work - just doesn't look current/professional enough. We do want to keep the pages after that clean, with come color but enough space for text and graphics.
Target Market(s)
Senior mgmt and HR executives in small-mid sized companies
Font styles to use
Sans Serif
Requirements
Must have
- Professional
- Clean
- Tied to company color scheme/logo
Nice to have
- Our title pages don't usually have many words on them; we'd like a design that has a lot of color - probably still using mainly our blue but accented with other colors.
- Need simple but smart looking pages after cover with lot of space; mostly we have text on the slides. Currently this is often in bullet point style, but we could probably upgrade the options there.
Should not have
- Anything that looks like a marketing style, as we typically use these with our current clients to share results of data collected, project plans, etc.

```html
<!DOCTYPE html>
<html lang="en">
<head>
<meta charset="utf-8">
<title>Kestrel Slide Template</title>
<link href="https://fonts.googleapis.com/css2?family=Roboto:wght@500;700&family=Open+Sans:wght@400;600&display=swap" rel="stylesheet">
<style>
:root{
  --navy:#2c5a95;
  --navy-dark:#1f4b7e;
  --deep:#17455e;
  --orange:#ef8a5a;
  --teal:#6db3a6;
  --ink:#333a44;
  --stage:#a9a7a8;
  --head:'Roboto',sans-serif;
  --body:'Open Sans',sans-serif;
}
*{margin:0;padding:0;box-sizing:border-box}
html,body{width:1200px;height:1200px;overflow:hidden;background:var(--stage)}
.board{position:relative;width:1200px;height:1200px}
.slide{position:absolute;width:281px;height:210px;background:#fff;overflow:hidden;font-family:var(--body);color:var(--ink)}
.c1{left:14px}.c2{left:310px}.c3{left:611px}.c4{left:909px}
.r1{top:30px}.r2{top:265px}.r3{top:494px}.r4{top:724px}.r5{top:955px}
.abs{position:absolute}
.ttl{position:absolute;left:13px;top:8px;font:700 9.5px/1 var(--head);color:var(--navy);letter-spacing:.2px}
.sub{font:500 5px/1.3 var(--head);color:var(--orange)}
.h{font:500 6.3px/1.3 var(--head);color:var(--navy)}
.h.o{color:var(--orange)}.h.t{color:var(--teal)}
.tx{font-size:4px;line-height:1.4;color:var(--ink)}
.tx.w{color:#fff}
.row{display:flex;gap:5px}
.foot{position:absolute;left:10px;right:3px;bottom:5px;height:8px;background:var(--navy);border-radius:0 4px 4px 0;display:flex;align-items:center;padding-left:4px;font:600 4.6px var(--body);color:#fff;letter-spacing:.8px}
.foot .brand{display:flex;align-items:center;width:118px}
.foot .brand i{width:5px;height:5px;border-radius:50%;background:#fff;margin-right:3px}
.foot .url{font-size:3px;letter-spacing:0;font-weight:400}
.foot b{position:absolute;right:0;top:0;height:8px;width:16px;border-radius:4px;background:var(--orange);font-size:3px;text-align:center;line-height:8px;font-weight:400}
.tag{position:absolute;right:4px;bottom:5px;display:flex;align-items:center;font:600 6px var(--body);color:#fff;letter-spacing:1.4px}
.tag b{margin-left:4px;height:8px;width:16px;border-radius:4px;background:var(--navy-dark);font-size:3px;text-align:center;line-height:8px;font-weight:400;letter-spacing:0}
.num{display:inline-flex;width:8px;height:8px;border-radius:50%;background:var(--navy);color:#fff;font-size:4.5px;align-items:center;justify-content:center;flex:none}
.dot{width:12px;height:12px;border-radius:50%;flex:none;display:flex;align-items:center;justify-content:center}
.dot::after{content:"";width:5px;height:4px;border:1px solid #fff;border-radius:1px}
.dot.lg{width:20px;height:20px}
.ring{width:20px;height:20px;border-radius:50%;border:1px solid var(--navy);flex:none}
.bg-n{background:var(--navy)}.bg-o{background:var(--orange)}.bg-t{background:var(--teal)}
.photo{position:absolute;left:0;right:0}
ul.bul{list-style:disc;padding-left:28px;font-size:3px;line-height:1.45;margin:3px 0 9px}
.quote{font:700 9.2px/1.35 var(--head);color:var(--navy)}
.quote .mk{font-size:14px;vertical-align:-3px}
.bignum{font:400 15px/1 var(--head);color:var(--navy)}
.bignum.o{color:var(--orange)}
.svc .h{font-size:5.5px}
.svc .tx{font-size:3.5px}
.card{height:66px;background:#e6e6e9;text-align:center;padding-top:6px}
.card .sq{display:inline-block;width:9px;height:8px;background:var(--navy);border-radius:1px}
.card .h{font-size:5px}
.card .tx{font-size:3.3px}
.diff .sub{font-size:5.3px}
.diff .tx{font-size:3.4px;margin:3px 0 7px}
</style>
</head>
<body>
<div class="board">

<!-- 11 Welcome, light -->
<section class="slide c1 r1">
  <div class="abs" style="top:25px;width:100%;text-align:center;font:700 9.5px var(--head);color:var(--navy)">WELCOME MESSAGE</div>
  <div class="abs" style="top:53px;left:0;right:0;height:95px;background:var(--navy-dark)"></div>
  <p class="abs tx w" style="top:84px;left:52px;width:178px;text-align:center;font-size:5.4px">Lorem ipsum dolor sit amet, consectetur adipiscing elit, sed do eiusmod tempor incididunt ut labore et dolore magna aliqua. Ut enim ad minim veniam, quis nostrud exercitation ullamco laboris nisi ut aliquip ex ea commodo consequat.</p>
  <div class="foot"><span class="brand"><span class="url">www.kestrelpartners.com</span></span><b>11</b></div>
</section>

<!-- 12 Welcome, photo band -->
<section class="slide c2 r1">
  <div class="photo" role="img" aria-label="City skyline at dusk tinted blue" style="top:28px;height:146px;background:linear-gradient(180deg,#3d6198,#2b5590)"></div>
  <div class="abs" style="top:61px;width:100%;text-align:center;font:700 9.5px var(--head);color:#fff">WELCOME MESSAGE</div>
  <p class="abs tx w" style="top:96px;left:52px;width:178px;text-align:center;font-size:5.4px">Lorem ipsum dolor sit amet, consectetur adipiscing elit, sed do eiusmod tempor incididunt ut labore et dolore magna aliqua. Ut enim ad minim veniam, quis nostrud exercitation ullamco laboris nisi ut aliquip ex ea commodo consequat.</p>
  <div class="foot"><span class="brand"><span class="url">www.kestrelpartners.com</span></span><b>12</b></div>
</section>

<!-- 13 Agenda numbered -->
<section class="slide c3 r1">
  <div class="ttl">AGENDA</div>
  <div class="abs" style="left:29px;top:27px;width:240px">
    <div class="row" style="margin-bottom:8px"><span class="num">1</span><div><div class="h">LOREM IPSUM DOLOR SIT AMET</div><div class="sub">LOREM IPSUM DOLOR SIT AMET, CONSECTETUR ADIPISCING ELIT</div><p class="tx">Lorem ipsum dolor sit amet, consectetuer adipiscing elit, sed diam nonummy<br>nibh euismod tincidunt ut laoreet dolore magna aliquam erat volutpat</p></div></div>
    <div class="row" style="margin-bottom:8px"><span class="num">2</span><div><div class="h">LOREM IPSUM DOLOR SIT AMET</div><div class="sub">LOREM IPSUM DOLOR SIT AMET, CONSECTETUR ADIPISCING ELIT</div><p class="tx">Lorem ipsum dolor sit amet, consectetuer adipiscing elit, sed diam nonummy<br>nibh euismod tincidunt ut laoreet dolore magna aliquam erat volutpat</p></div></div>
    <div class="row" style="margin-bottom:8px"><span class="num">3</span><div><div class="h">LOREM IPSUM DOLOR SIT AMET</div><div class="sub">LOREM IPSUM DOLOR SIT AMET, CONSECTETUR ADIPISCING ELIT</div><p class="tx">Lorem ipsum dolor sit amet, consectetuer adipiscing elit, sed diam nonummy<br>nibh euismod tincidunt ut laoreet dolore magna aliquam erat volutpat</p></div></div>
    <div class="row"><span class="num">4</span><div><div class="h">LOREM IPSUM DOLOR SIT AMET</div><div class="sub">LOREM IPSUM DOLOR SIT AMET, CONSECTETUR ADIPISCING ELIT</div><p class="tx">Lorem ipsum dolor sit amet, consectetuer adipiscing elit, sed diam nonummy<br>nibh euismod tincidunt ut laoreet dolore magna aliquam erat volutpat</p></div></div>
  </div>
  <div class="foot"><span class="brand"><i></i>KESTREL</span><span class="url">www.kestrelpartners.com</span><b>13</b></div>
</section>

<!-- 14 Agenda bullets -->
<section class="slide c4 r1">
  <div class="ttl">AGENDA</div>
  <div class="abs" style="left:33px;top:25px;width:235px">
    <div class="h">LOREM IPSUM DOLOR SIT AMET</div>
    <div class="sub" style="padding-left:16px">LOREM IPSUM DOLOR SIT AMET, CONSECTETUR ADIPISCING ELIT</div>
    <ul class="bul"><li>Lorem ipsum dolor sit amet, consectetuer adipiscing elit</li><li>Lorem ipsum dolor sit amet, consectetuer adipiscing elit</li><li>Lorem ipsum dolor sit amet, consectetuer adipiscing elit</li><li>Lorem ipsum dolor sit amet, consectetuer adipiscing elit</li></ul>
    <div class="h">LOREM IPSUM DOLOR SIT AMET</div>
    <div class="sub" style="padding-left:16px">LOREM IPSUM DOLOR SIT AMET, CONSECTETUR ADIPISCING ELIT</div>
    <ul class="bul"><li>Lorem ipsum dolor sit amet, consectetuer adipiscing elit</li><li>Lorem ipsum dolor sit amet, consectetuer adipiscing elit</li><li>Lorem ipsum dolor sit amet, consectetuer adipiscing elit</li><li>Lorem ipsum dolor sit amet, consectetuer adipiscing elit</li></ul>
    <div class="h">LOREM IPSUM DOLOR SIT AMET</div>
    <div class="sub" style="padding-left:16px">LOREM IPSUM DOLOR SIT AMET, CONSECTETUR ADIPISCING ELIT</div>
    <ul class="bul" style="margin-bottom:0"><li>Lorem ipsum dolor sit amet, consectetuer adipiscing elit</li><li>Lorem ipsum dolor sit amet, consectetuer adipiscing elit</li><li>Lorem ipsum dolor sit amet, consectetuer adipiscing elit</li><li>Lorem ipsum dolor sit amet, consectetuer adipiscing elit</li></ul>
  </div>
  <div class="foot"><span class="brand"><i></i>KESTREL</span><span class="url">www.kestrelpartners.com</span><b>14</b></div>
</section>

<!-- 15 Title here list -->
<section class="slide c1 r2">
  <div class="ttl">TITLE HERE</div>
  <div class="abs sub" style="left:13px;top:21px">SUB TITLE &nbsp;SUB TITLE &nbsp;&nbsp;SUB TITLE &nbsp;&nbsp;SUB TITLE</div>
  <div class="abs" style="left:41px;top:49px;width:200px">
    <div class="row" style="gap:6px;margin-bottom:7px"><span class="num">1</span><div><div class="h" style="font-size:4.6px">LOREM IPSUM DOLOR SIT AMET, CONSECTETUR ADIPISCING ELIT</div><p class="tx" style="font-size:3.2px">Lorem ipsum dolor sit amet, consectetuer adipiscing elit, sed diam nonummy nibh euismod<br>tincidunt ut laoreet dolore magna aliquam erat volutpat</p></div></div>
    <div class="row" style="gap:6px;margin-bottom:7px"><span class="num">2</span><div><div class="h" style="font-size:4.6px">LOREM IPSUM DOLOR SIT AMET, CONSECTETUR ADIPISCING ELIT</div><p class="tx" style="font-size:3.2px">Lorem ipsum dolor sit amet, consectetuer adipiscing elit, sed diam nonummy nibh euismod<br>tincidunt ut laoreet dolore magna aliquam erat volutpat</p></div></div>
    <div class="row" style="gap:6px;margin-bottom:7px"><span class="num">3</span><div><div class="h" style="font-size:4.6px">LOREM IPSUM DOLOR SIT AMET, CONSECTETUR ADIPISCING ELIT</div><p class="tx" style="font-size:3.2px">Lorem ipsum dolor sit amet, consectetuer adipiscing elit, sed diam nonummy nibh euismod<br>tincidunt ut laoreet dolore magna aliquam erat volutpat</p></div></div>
    <div class="row" style="gap:6px;margin-bottom:7px"><span class="num">4</span><div><div class="h" style="font-size:4.6px">LOREM IPSUM DOLOR SIT AMET, CONSECTETUR ADIPISCING ELIT</div><p class="tx" style="font-size:3.2px">Lorem ipsum dolor sit amet, consectetuer adipiscing elit, sed diam nonummy nibh euismod<br>tincidunt ut laoreet dolore magna aliquam erat volutpat</p></div></div>
    <div class="row" style="gap:6px"><span class="num">5</span><div><div class="h" style="font-size:4.6px">LOREM IPSUM DOLOR SIT AMET, CONSECTETUR ADIPISCING ELIT</div><p class="tx" style="font-size:3.2px">Lorem ipsum dolor sit amet, consectetuer adipiscing elit, sed diam nonummy nibh euismod<br>tincidunt ut laoreet dolore magna aliquam erat volutpat</p></div></div>
  </div>
  <div class="foot"><span class="brand"><i></i>KESTREL</span><span class="url">www.kestrelpartners.com</span><b>15</b></div>
</section>

<!-- 16 Table of content -->
<section class="slide c2 r2">
  <div class="ttl">TABLE OF CONTENT</div>
  <div class="abs" style="left:26px;top:52px;display:grid;grid-template-columns:122px 110px;row-gap:18px">
    <div class="row"><span class="bignum">1</span><div><div class="h" style="font-size:5px">LOREM IPSUM</div><p class="tx" style="font-size:4.6px">Lorem ipsum dolor sit amet,<br>consectetur adipiscing elit</p></div></div>
    <div class="row"><span class="bignum o">4</span><div><div class="h o" style="font-size:5px">LOREM IPSUM</div><p class="tx" style="font-size:4.6px">Lorem ipsum dolor sit amet,<br>consectetur adipiscing elit</p></div></div>
    <div class="row"><span class="bignum">2</span><div><div class="h" style="font-size:5px">LOREM IPSUM</div><p class="tx" style="font-size:4.6px">Lorem ipsum dolor sit amet,<br>consectetur adipiscing elit</p></div></div>
    <div class="row"><span class="bignum o">5</span><div><div class="h o" style="font-size:5px">LOREM IPSUM</div><p class="tx" style="font-size:4.6px">Lorem ipsum dolor sit amet,<br>consectetur adipiscing elit</p></div></div>
    <div class="row"><span class="bignum">3</span><div><div class="h" style="font-size:5px">LOREM IPSUM</div><p class="tx" style="font-size:4.6px">Lorem ipsum dolor sit amet,<br>consectetur adipiscing elit</p></div></div>
    <div class="row"><span class="bignum o">6</span><div><div class="h o" style="font-size:5px">LOREM IPSUM</div><p class="tx" style="font-size:4.6px">Lorem ipsum dolor sit amet,<br>consectetur adipiscing elit</p></div></div>
  </div>
  <div class="foot"><span class="brand"><i></i>KESTREL</span><span class="url">www.kestrelpartners.com</span><b>16</b></div>
</section>

<!-- 17 Icon grid -->
<section class="slide c3 r2">
  <div class="ttl">TITLE HERE</div>
  <div class="abs" style="left:10px;top:46px;display:grid;grid-template-columns:90px 90px 90px;row-gap:20px">
    <div class="row" style="gap:4px"><span class="dot bg-n"></span><div><div class="h" style="font-size:5px">LOREM IPSUM</div><p class="tx">Lorem ipsum dolor sit amet,<br>consectetur adipiscing elit</p></div></div>
    <div class="row" style="gap:4px"><span class="dot bg-o"></span><div><div class="h o" style="font-size:5px">LOREM IPSUM</div><p class="tx">Lorem ipsum dolor sit amet,<br>consectetur adipiscing elit</p></div></div>
    <div class="row" style="gap:4px"><span class="dot bg-t"></span><div><div class="h t" style="font-size:5px">LOREM IPSUM</div><p class="tx">Lorem ipsum dolor sit amet,<br>consectetur adipiscing elit</p></div></div>
    <div class="row" style="gap:4px"><span class="dot bg-n"></span><div><div class="h" style="font-size:5px">LOREM IPSUM</div><p class="tx">Lorem ipsum dolor sit amet,<br>consectetur adipiscing elit</p></div></div>
    <div class="row" style="gap:4px"><span class="dot bg-o"></span><div><div class="h o" style="font-size:5px">LOREM IPSUM</div><p class="tx">Lorem ipsum dolor sit amet,<br>consectetur adipiscing elit</p></div></div>
    <div class="row" style="gap:4px"><span class="dot bg-t"></span><div><div class="h t" style="font-size:5px">LOREM IPSUM</div><p class="tx">Lorem ipsum dolor sit amet,<br>consectetur adipiscing elit</p></div></div>
    <div class="row" style="gap:4px"><span class="dot bg-n"></span><div><div class="h" style="font-size:5px">LOREM IPSUM</div><p class="tx">Lorem ipsum dolor sit amet,<br>consectetur adipiscing elit</p></div></div>
    <div class="row" style="gap:4px"><span class="dot bg-o"></span><div><div class="h o" style="font-size:5px">LOREM IPSUM</div><p class="tx">Lorem ipsum dolor sit amet,<br>consectetur adipiscing elit</p></div></div>
    <div class="row" style="gap:4px"><span class="dot bg-t"></span><div><div class="h t" style="font-size:5px">LOREM IPSUM</div><p class="tx">Lorem ipsum dolor sit amet,<br>consectetur adipiscing elit</p></div></div>
  </div>
  <div class="foot"><span class="brand"><i></i>KESTREL</span><span class="url">www.kestrelpartners.com</span><b>17</b></div>
</section>

<!-- 18 About us, banner photo -->
<section class="slide c4 r2">
  <div class="ttl">ABOUT US</div>
  <div class="photo" role="img" aria-label="Boardroom with conference table and chairs tinted blue" style="top:30px;height:96px;background:linear-gradient(180deg,#7b93d6,#4e67a8 70%,#3d5590)"></div>
  <p class="abs tx" style="left:13px;top:140px;width:120px;font-size:5.3px">Lorem ipsum dolor sit amet, consectetuer adipiscing elit, sed diam nonummy nibh euismod tincidunt ut laoreet dolore magna aliquam erat volutpat</p>
  <div class="abs" style="left:158px;top:139px;display:flex;gap:20px"><span class="dot lg bg-n"></span><span class="dot lg bg-n"></span><span class="dot lg bg-n"></span></div>
  <div class="foot"><span class="brand"><i></i>KESTREL</span><span class="url">www.kestrelpartners.com</span><b>18</b></div>
</section>

<!-- 19 About us, centered -->
<section class="slide c1 r3">
  <div class="ttl">ABOUT US</div>
  <div class="photo" role="img" aria-label="Boardroom with leather chairs and city windows" style="top:30px;height:96px;background:linear-gradient(180deg,#d8d4cf,#9a8a78 55%,#5a4535)"></div>
  <div class="abs" style="left:84px;top:115px;display:flex;gap:19px"><span class="dot lg bg-n"></span><span class="dot lg bg-n"></span><span class="dot lg bg-n"></span></div>
  <p class="abs tx" style="left:75px;top:148px;width:130px;text-align:center;font-size:5.3px">Lorem ipsum dolor sit amet, consectetuer adipiscing elit, sed diam nonummy nibh euismod tincidunt ut laoreet dolore magna aliquam erat volutpat</p>
  <div class="foot"><span class="brand"><i></i>KESTREL</span><span class="url">www.kestrelpartners.com</span><b>19</b></div>
</section>

<!-- 20 Divider navy -->
<section class="slide c2 r3" style="background:var(--navy)">
  <div class="abs" style="left:59px;top:74px;font:700 9.4px var(--head);color:#fff">PAIRING PRECISION WITH EXPERIENCE</div>
  <p class="abs tx w" style="left:59px;top:96px;width:165px;font-size:5.4px">Our advisory group brings together specialists in areas from strategy to learning design to behavioral science, so every engagement is shaped carefully around the goals of each organization we serve.</p>
  <div class="tag">KESTREL<b style="background:var(--orange)">20</b></div>
</section>

<!-- 21 Divider teal -->
<section class="slide c3 r3" style="background:var(--teal)">
  <div class="abs" style="left:59px;top:74px;font:700 9.4px var(--head);color:var(--navy)">PAIRING PRECISION WITH EXPERIENCE</div>
  <p class="abs tx" style="left:59px;top:96px;width:165px;font-size:5.4px;color:var(--navy)">Our advisory group brings together specialists in areas from strategy to learning design to behavioral science, so every engagement is shaped carefully around the goals of each organization we serve.</p>
  <div class="tag">KESTREL<b>21</b></div>
</section>

<!-- 22 Quote lavender -->
<section class="slide c4 r3" role="img" aria-label="Soft lavender backdrop of a person at a laptop" style="background:linear-gradient(135deg,#eceaf3,#dcd9e8)">
  <div class="abs quote" style="left:53px;top:72px;width:190px"><span class="mk">&ldquo;</span> GREAT RESULTS START WITH<br>&nbsp;&nbsp;&nbsp;&nbsp;GREAT PEOPLE ON THE TEAM.<br><br>&nbsp;&nbsp;&nbsp;&nbsp;HOW STRONG IS YOUR TEAM? <span class="mk">&rdquo;</span></div>
  <div class="tag" style="color:var(--navy)">KESTREL<b>22</b></div>
</section>

<!-- 23 Quote orange -->
<section class="slide c1 r4" style="background:var(--orange)">
  <div class="abs quote" style="left:53px;top:72px;width:190px"><span class="mk">&ldquo;</span> GREAT RESULTS START WITH<br>&nbsp;&nbsp;&nbsp;&nbsp;GREAT PEOPLE ON THE TEAM.<br><br>&nbsp;&nbsp;&nbsp;&nbsp;HOW STRONG IS YOUR TEAM? <span class="mk">&rdquo;</span></div>
  <div class="tag">KESTREL<b>23</b></div>
</section>

<!-- 24 Services navy -->
<section class="slide c2 r4" style="background:var(--navy)">
  <div class="ttl" style="color:var(--orange)">OUR SERVICES</div>
  <div class="abs svc" style="left:26px;top:48px;display:grid;grid-template-columns:122px 110px;row-gap:14px">
    <div class="row"><span class="dot lg bg-o"></span><div><div class="h o">IT Leadership</div><p class="tx w">We help seasoned technical<br>specialists grow into confident<br>business leaders across<br>a focused six-month track</p></div></div>
    <div class="row"><span class="dot lg bg-o"></span><div><div class="h o">Profile Certification</div><p class="tx w">Learn how people approach<br>problems, routines and pace,<br>and how to work with others,<br>taught by the team that<br>built the Kestrel<br>Profile</p></div></div>
    <div class="row"><span class="dot lg bg-o"></span><div><div class="h o">Kestrel Management<br>School</div><p class="tx w">We move new managers<br>along a guided growth path<br>with hands-on practice sessions<br>run by experienced leaders<br>over one focused month of<br>learning</p></div></div>
    <div class="row"><span class="dot lg bg-o"></span><div><div class="h o">Supplier Insight Review</div><p class="tx w">Receive a clear report with<br>scored summaries and next<br>actions covering key areas of<br>reliability, trust, quality,<br>openness, communication,<br>and more.</p></div></div>
  </div>
  <div class="foot" style="background:#e9e9ee;color:var(--navy)"><span class="brand"><i style="background:var(--navy)"></i>KESTREL</span><span class="url" style="color:var(--navy)">www.kestrelpartners.com</span><b>24</b></div>
</section>

<!-- 25 Services white -->
<section class="slide c3 r4">
  <div class="ttl">OUR SERVICES</div>
  <div class="abs svc" style="left:26px;top:48px;display:grid;grid-template-columns:122px 110px;row-gap:14px">
    <div class="row"><span class="ring"></span><div><div class="h">IT Leadership</div><p class="tx">We help seasoned technical<br>specialists grow into confident<br>business leaders across<br>a focused six-month track</p></div></div>
    <div class="row"><span class="ring"></span><div><div class="h">Profile Certification</div><p class="tx">Learn how people approach<br>problems, routines and pace,<br>and how to work with others,<br>taught by the team that<br>built the Kestrel<br>Profile</p></div></div>
    <div class="row"><span class="ring"></span><div><div class="h">Kestrel Management<br>School</div><p class="tx">We move new managers<br>along a guided growth path<br>with hands-on practice sessions<br>run by experienced leaders<br>over one focused month of<br>learning</p></div></div>
    <div class="row"><span class="ring"></span><div><div class="h">Supplier Insight Review</div><p class="tx">Receive a clear report with<br>scored summaries and next<br>actions covering key areas of<br>reliability, trust, quality,<br>openness, communication,<br>and more.</p></div></div>
  </div>
  <div class="foot"><span class="brand"><i></i>KESTREL</span><span class="url">www.kestrelpartners.com</span><b>25</b></div>
</section>

<!-- 26 Services ring -->
<section class="slide c4 r4">
  <div class="ttl">OUR SERVICES</div>
  <svg class="abs" style="left:95px;top:45px" width="90" height="90" viewBox="0 0 90 90">
    <path d="M45 3A42 42 0 0 1 87 45H62A17 17 0 0 0 45 28Z" fill="var(--orange)"/>
    <path d="M87 45A42 42 0 0 1 45 87V62A17 17 0 0 0 62 45Z" fill="var(--deep)"/>
    <path d="M45 87A42 42 0 0 1 3 45H28A17 17 0 0 0 45 62Z" fill="var(--teal)"/>
    <path d="M3 45A42 42 0 0 1 45 3V28A17 17 0 0 0 28 45Z" fill="var(--navy)"/>
    <circle cx="45" cy="45" r="14" fill="#fff" stroke="#dde" stroke-width="1"/>
    <circle cx="45" cy="45" r="8" fill="none" stroke="var(--navy)" stroke-width="1.2"/>
    <circle cx="45" cy="16" r="6" fill="#fff"/><circle cx="74" cy="45" r="6" fill="#fff"/><circle cx="45" cy="74" r="6" fill="#fff"/><circle cx="16" cy="45" r="6" fill="#fff"/>
  </svg>
  <div class="abs svc" style="left:20px;top:44px;width:70px;text-align:right"><span style="display:inline-block;width:8px;height:7px;background:var(--navy);border-radius:1px"></span><div class="h">IT Leadership</div><p class="tx" style="font-size:3.3px">We help seasoned technical specialists grow into confident business leaders across a focused six-month track</p></div>
  <div class="abs svc" style="left:20px;top:104px;width:70px;text-align:right"><span style="display:inline-block;width:8px;height:7px;background:var(--teal);border-radius:1px"></span><div class="h t">Kestrel<br>Management School</div><p class="tx" style="font-size:3.3px">We move new managers along a guided growth path with hands-on practice sessions run by experienced leaders over one focused month</p></div>
  <div class="abs svc" style="left:192px;top:44px;width:74px"><span style="display:block;width:8px;height:7px;background:var(--orange);border-radius:1px;margin-bottom:2px"></span><div class="h o">Profile Certification</div><p class="tx" style="font-size:3.3px">Learn how people approach problems, routines and pace, and how to work with others, taught by the team that built the Kestrel Profile</p></div>
  <div class="abs svc" style="left:192px;top:108px;width:74px"><div class="h" style="color:var(--deep)">Supplier<br>Insight Review</div><p class="tx" style="font-size:3.3px">Receive a clear report with scored summaries and next actions covering reliability, trust, quality, openness, communication, and more.</p></div>
  <div class="foot"><span class="brand"><i></i>KESTREL</span><span class="url">www.kestrelpartners.com</span><b>26</b></div>
</section>

<!-- 27 Services cards -->
<section class="slide c1 r5">
  <div class="ttl">OUR SERVICES</div>
  <div class="abs" style="left:34px;top:32px;display:grid;grid-template-columns:100px 100px;gap:10px 13px">
    <div class="card" role="img" aria-label="Faded photo of a person working at a computer"><span class="sq"></span><div class="h">IT Leadership</div><p class="tx">We help seasoned technical<br>specialists grow into confident<br>business leaders across<br>a focused six-month track</p></div>
    <div class="card" role="img" aria-label="Faded photo of a laptop on a desk" style="background:#ececee"><span class="sq"></span><div class="h">Profile Certification</div><p class="tx">Learn how people approach problems,<br>routines and pace, and how to work<br>with others, taught by the team<br>that built the Kestrel Profile</p></div>
    <div class="card" role="img" aria-label="Faded photo of managers in a meeting"><span class="sq"></span><div class="h">Kestrel Management School</div><p class="tx">We move new managers along a<br>guided growth path with hands-on<br>practice sessions run by<br>experienced leaders over one<br>focused month of learning</p></div>
    <div class="card" role="img" aria-label="Faded photo of a handshake" style="background:#e9e9ec"><span class="sq"></span><div class="h">Supplier Insight Review</div><p class="tx">Receive a clear report with scored<br>summaries and next actions covering<br>reliability, trust, quality,<br>openness, communication,<br>and more.</p></div>
  </div>
  <div class="foot"><span class="brand"><i></i>KESTREL</span><span class="url">www.kestrelpartners.com</span><b>27</b></div>
</section>

<!-- 28 Difference, three circles -->
<section class="slide c2 r5">
  <div class="ttl">THE KESTREL DIFFERENCE</div>
  <div class="abs diff" style="left:26px;top:40px;width:110px">
    <div class="sub">PEOPLE-FIRST, EVIDENCE-BASED</div>
    <p class="tx">Our methods rest on tested research and sound assessment models, yet each one is built for the real day-to-day demands of a business that keeps changing. Joining rigor with practical use is what sets our approach apart.</p>
    <div class="sub">ROLE-SPECIFIC</div>
    <p class="tx">Many tools are shallow and sort people into a handful of generic types. We take a finer view, using a set of clear measures to capture the details of each person's working style, results, drivers, and how they see themselves.</p>
    <div class="sub" style="color:var(--navy)">LASTING &amp; ADAPTABLE</div>
    <p class="tx" style="margin-bottom:0">Clients stay with us for many years because they see our tools, programs, and services lower their costs while lifting their results. We value long relationships, and many partners have worked with us for two decades.</p>
  </div>
  <svg class="abs" style="left:144px;top:50px" width="116" height="116" viewBox="0 0 116 116">
    <circle cx="36" cy="38" r="33" fill="var(--teal)" opacity=".85"/>
    <circle cx="80" cy="38" r="33" fill="var(--orange)" opacity=".85"/>
    <circle cx="58" cy="76" r="33" fill="var(--navy)" opacity=".85"/>
    <rect x="30" y="32" width="11" height="9" fill="none" stroke="#fff" stroke-width="1.2"/>
    <circle cx="84" cy="36" r="5" fill="none" stroke="#fff" stroke-width="1.2"/>
    <circle cx="58" cy="83" r="5" fill="none" stroke="#fff" stroke-width="1.2"/>
  </svg>
  <div class="foot"><span class="brand"><i></i>KESTREL</span><span class="url">www.kestrelpartners.com</span><b>28</b></div>
</section>

<!-- 29 Difference, overlapping rings -->
<section class="slide c3 r5">
  <div class="ttl">THE KESTREL DIFFERENCE</div>
  <div class="abs diff" style="left:28px;top:37px;width:110px">
    <div class="sub">PEOPLE-FIRST, EVIDENCE-BASED</div>
    <p class="tx">Our methods rest on tested research and sound assessment models, yet each one is built for the real day-to-day demands of a business that keeps changing. Joining rigor with practical use is what sets our approach apart.</p>
    <div class="sub">ROLE-SPECIFIC</div>
    <p class="tx">Many tools are shallow and sort people into a handful of generic types. We take a finer view, using a set of clear measures to capture the details of each person's working style, results, drivers, and how they see themselves.</p>
    <div class="sub" style="color:var(--navy)">LASTING &amp; ADAPTABLE</div>
    <p class="tx" style="margin-bottom:0">Clients stay with us for many years because they see our tools, programs, and services lower their costs while lifting their results. We value long relationships, and many partners have worked with us for two decades.</p>
  </div>
  <svg class="abs" style="left:148px;top:43px" width="110" height="110" viewBox="0 0 110 110">
    <circle cx="55" cy="37" r="34" fill="var(--navy)" stroke="#fff" stroke-width="1.5"/>
    <circle cx="37" cy="70" r="34" fill="var(--teal)" stroke="#fff" stroke-width="1.5"/>
    <circle cx="73" cy="70" r="34" fill="var(--orange)" stroke="#fff" stroke-width="1.5"/>
    <circle cx="55" cy="37" r="34" fill="none" stroke="#fff" stroke-width="1.5"/>
    <circle cx="37" cy="70" r="34" fill="none" stroke="#fff" stroke-width="1.5"/>
    <circle cx="55" cy="58" r="12" fill="#fff"/>
    <circle cx="55" cy="58" r="7" fill="none" stroke="var(--navy)" stroke-width="1.2"/>
    <rect x="50" y="16" width="11" height="9" fill="none" stroke="#fff" stroke-width="1.2"/>
    <circle cx="24" cy="80" r="4.5" fill="none" stroke="#fff" stroke-width="1.2"/>
    <circle cx="87" cy="80" r="4.5" fill="none" stroke="#fff" stroke-width="1.2"/>
  </svg>
  <div class="foot"><span class="brand"><i></i>KESTREL</span><span class="url">www.kestrelpartners.com</span><b>29</b></div>
</section>

<!-- 30 Difference, stacked items -->
<section class="slide c4 r5">
  <div class="ttl">THE KESTREL DIFFERENCE</div>
  <div class="abs diff" style="left:37px;top:41px;width:210px">
    <div class="row" style="gap:6px;margin-bottom:14px"><span class="dot lg bg-t"></span><div><div class="sub">PEOPLE-FIRST, EVIDENCE-BASED</div><p class="tx" style="margin:0">Our methods rest on tested research and sound assessment models, yet each one is built for the real day-to-day demands of a business that keeps changing. Joining rigor with practical use is what sets our approach apart.</p></div></div>
    <div class="row" style="gap:6px;margin-bottom:14px"><span class="dot lg bg-n"></span><div><div class="sub" style="color:var(--navy)">LASTING &amp; ADAPTABLE</div><p class="tx" style="margin:0">Clients stay with us for many years because they see our tools, programs, and services lower their costs while lifting their results. We value long relationships, and many partners have worked with us for two decades.</p></div></div>
    <div class="row" style="gap:6px"><span class="dot lg bg-o"></span><div><div class="sub">ROLE-SPECIFIC</div><p class="tx" style="margin:0">Many tools are shallow and sort people into a handful of generic types. We take a finer view, using a set of clear measures to capture the details of each person's working style, results, drivers, and self-view.</p></div></div>
  </div>
  <div class="foot"><span class="brand"><i></i>KESTREL</span><span class="url">www.kestrelpartners.com</span><b>30</b></div>
</section>

</div>
</body>
</html>
```